Flyer für den Bereich Solarenergie
Zielgruppe
Guten Tag,
wir sind im Bereich Solarenergie tätig. Wir suchen nun Hallen mit großen Dächern, die wir anmieten können, um darauf Solaranlagen zu bauen. Wir machen dabei alles aus einer Hand. der Eigentümer muss nichts machen. Er bekommt sogar Geld von uns und das Dach ist sowieso meistens leer.
Aufgabenstellung
Wir möchten einen DINA4 Flyer den wir als PDF in Emails verschicken können. Farbdaten sollten Sie aus den Logodateien im Anhang entnehmen können. Richten Sie sich auch gerne an das Design des Logos und der Website. Dabei sollen kurz die wichtigsten Key Faktoren aufgelistet werden und das Unternehmen kurz dargestellt werden. Hier einmal die Texte:
Beschreibung zum Unternehmen:
Veltrano ist Experte für grüne Energietechnik mit über 20 Jahren Erfahrung. Mit über 1.000 zufriedenen Kunden im Bereich Photovoltaikanlagen können wir auf einen großen Erfahrungsschatz zurückgreifen. Wenn wir am Werk sind, wird nicht nur das Klima geschont, sondern auch Sie als Kunde profitieren. Mit uns wird nachhaltiges Handeln kinderleicht und gleichzeitig rentabel.
Erwirtschaften auch Sie mit Ihrem Dach nun bares Geld!
Ihre Vorteile:
- Umwelt schonen durch das Produzieren von grünem Strom
- Dach schützen vor Emissionen
- Dachsanierungen anstatt von Mietzahlungen möglich
- Keine Kosten, da wir alle Kosten der Anträge, der Anlage und aller Arbeiten übernehmen
- Mieteinnahmen generieren!
Einzige Voraussetzung:
Dachfläche mit mind. 1.500qm
Worauf warten Sie?
Nehmen Sie jetzt Kontakt auf für eine entsprechende Machbarkeitsprüfung. Natürlich ist auch das Kostenlos.
veltrano GmbH
Fennstraße 47b
48155 Münster
T: +49 176 528 914 03
E: info@veltrano-beispiel.de

```html
<!DOCTYPE html>
<html lang="de">
<head>
<meta charset="utf-8">
<title>Veltrano – Flyer Solarenergie</title>
<link href="https://fonts.googleapis.com/css2?family=Inter:wght@300;400;700;800&display=swap" rel="stylesheet">
<style>
  :root {
    --stage: #2b303f;
    --navy: #1b2744;
    --navy-deep: #14203a;
    --green: #b1cb10;
    --ink: #333a40;
    --text: #4e5458;
    --panel: #f8f8f8;
    --white: #ffffff;
    --line: #c9c9c9;
  }
  * { box-sizing: border-box; margin: 0; padding: 0; }
  html, body { width: 1200px; height: 1130px; overflow: hidden; background: var(--stage); }
  body { font-family: "Inter", sans-serif; position: relative; }

  .flyer {
    position: absolute; left: 200px; top: 0;
    width: 938px; height: 1327px;
    transform: scale(0.8515); transform-origin: top left;
    background: var(--white); overflow: hidden;
  }

  /* header */
  .hero { position: absolute; left: 0; top: 0; width: 938px; height: 313px; }
  .hero-photo {
    position: absolute; inset: 0;
    background: linear-gradient(170deg, #8a6f5a 0%, #4d5a73 6%, #34476b 25%, #243556 55%, var(--navy-deep) 100%);
  }
  .brand { position: absolute; left: 45px; top: 48px; color: var(--white); font-weight: 300; font-size: 40px; letter-spacing: 0.5px; }
  .hero-title { position: absolute; left: 45px; top: 156px; color: var(--white); font-weight: 800; font-size: 42px; letter-spacing: -0.3px; }
  .hero-sub { position: absolute; left: 46px; top: 212px; color: var(--green); font-weight: 300; font-size: 27px; }
  .accent-bar { position: absolute; left: 0; top: 300px; width: 699px; height: 13px; background: var(--green); }

  /* intro */
  .intro { position: absolute; left: 0; top: 313px; width: 938px; height: 319px; }
  .intro-heading { position: absolute; left: 45px; top: 45px; font-size: 26px; font-weight: 700; line-height: 31px; color: var(--ink); }
  .intro-body { position: absolute; left: 45px; top: 138px; width: 610px; font-size: 18px; line-height: 28px; color: var(--text); }
  .intro-photo {
    position: absolute; left: 699px; top: 0; width: 239px; height: 319px;
    background: linear-gradient(180deg, #dfe3e6 0%, #c9d0d4 35%, #7f8a94 45%, #4a5f8f 60%, #2f4585 100%);
  }

  /* advantages */
  .benefits { position: absolute; left: 0; top: 632px; width: 938px; height: 482px; background: var(--panel); }
  .benefits-title { position: absolute; left: 45px; top: 32px; font-size: 26px; font-weight: 700; color: var(--ink); }
  .benefit {
    position: absolute; width: 430px; height: 105px; background: var(--white);
    box-shadow: 0 1px 4px rgba(0,0,0,0.05);
    display: flex; align-items: center; padding-left: 111px;
    font-size: 17px; line-height: 21px; color: var(--text); letter-spacing: 0.2px;
  }
  .benefit svg { position: absolute; left: 22px; top: 33px; width: 40px; height: 40px; }
  .col-left { left: 25px; } .col-right { left: 482px; padding-left: 87px; }
  .col-right svg { left: 22px; }
  .row-1 { top: 96px; } .row-2 { top: 221px; } .row-3 { top: 345px; }
  .requirement {
    position: absolute; left: 482px; top: 345px; width: 430px; height: 105px;
    border: 1.5px dashed var(--line); border-radius: 4px;
    display: flex; flex-direction: column; align-items: center; justify-content: center;
    font-size: 17px; color: var(--text); gap: 6px;
  }
  .requirement strong { color: var(--green); font-size: 19px; font-weight: 700; }

  /* footer */
  .contact { position: absolute; left: 0; top: 1114px; width: 938px; height: 213px; background: var(--green); color: var(--white); }
  .contact-heading { position: absolute; left: 45px; top: 42px; font-size: 26px; font-weight: 700; }
  .contact-rule { position: absolute; left: 45px; top: 86px; width: 80px; height: 3px; background: var(--white); }
  .contact-body { position: absolute; left: 45px; top: 122px; width: 500px; font-size: 18px; line-height: 26px; }
  .contact-details { position: absolute; left: 597px; top: 42px; font-size: 18px; line-height: 24px; }
  .contact-line { display: flex; align-items: center; gap: 12px; margin-top: 12px; }
  .contact-line:first-of-type { margin-top: 22px; }
  .contact-line svg { width: 20px; height: 20px; }
</style>
</head>
<body>
  <article class="flyer">
    <header class="hero">
      <div class="hero-photo" role="img" aria-label="Großes Solarfeld mit Photovoltaikmodulen in der Abenddämmerung"></div>
      <div class="brand">veltrano</div>
      <h1 class="hero-title">Ihr Experte für grüne Energietechnik</h1>
      <p class="hero-sub">Seit über 20 Jahren</p>
      <div class="accent-bar"></div>
    </header>

    <section class="intro">
      <h2 class="intro-heading">Erwirtschaften auch Sie mit Ihrem<br>Dach bares Geld!</h2>
      <p class="intro-body">Mit über 1.000 zufriedenen Kunden im Bereich Photovoltaikanlagen können wir auf einen großen Erfahrungsschatz zurückgreifen. Wenn wir am Werk sind, wird nicht nur das Klima geschont, sondern auch Sie als Kunde profitieren. Mit uns wird nachhaltiges Handeln kinderleicht und gleichzeitig rentabel.</p>
      <div class="intro-photo" role="img" aria-label="Solarmodule auf einem Flachdach mit Stadtsilhouette im Hintergrund"></div>
    </section>

    <section class="benefits">
      <h2 class="benefits-title">Ihre Vorteile auf einem Blick:</h2>

      <div class="benefit col-left row-1">
        <svg viewBox="0 0 40 40"><path d="M20 4 L35 9 V20 C35 29 28 34 20 37 C12 34 5 29 5 20 V9 Z" fill="var(--green)"/><path d="M13 20 L18 25 L27 15" stroke="#fff" stroke-width="3" fill="none" stroke-linecap="round" stroke-linejoin="round"/></svg>
        Dach schützen vor Emissionen
      </div>
      <div class="benefit col-right row-1">
        <svg viewBox="0 0 40 40"><path d="M23 3 L8 23 H19 L15 37 L32 16 H21 Z" fill="var(--green)"/></svg>
        Umwelt schonen durch das<br>Produzieren von grünem Strom
      </div>
      <div class="benefit col-left row-2">
        <svg viewBox="0 0 40 40"><circle cx="20" cy="20" r="18" fill="var(--green)"/><text x="20" y="27" text-anchor="middle" font-family="Inter, sans-serif" font-size="20" font-weight="700" fill="#fff">€</text></svg>
        Mieteinnahmen generieren
      </div>
      <div class="benefit col-right row-2">
        <svg viewBox="0 0 40 40"><rect x="3" y="3" width="12" height="12" rx="2" fill="var(--green)"/><rect x="25" y="25" width="12" height="12" rx="2" fill="var(--green)"/><path d="M34 16 V10 H24 M27 7 L24 10 L27 13" stroke="var(--green)" stroke-width="2.5" fill="none" stroke-linecap="round" stroke-linejoin="round"/><path d="M6 24 V30 H16 M13 27 L16 30 L13 33" stroke="var(--green)" stroke-width="2.5" fill="none" stroke-linecap="round" stroke-linejoin="round"/></svg>
        Dachsanierungen anstatt von<br>Mietzahlungen möglich
      </div>
      <div class="benefit col-left row-3">
        <svg viewBox="0 0 40 40"><path d="M14 3 H26 L34 11 V30 H14 Z" fill="var(--green)" opacity="0.6"/><path d="M7 9 H20 L28 17 V37 H7 Z" fill="var(--green)"/><rect x="11" y="26" width="9" height="2.5" fill="#fff"/><rect x="11" y="31" width="9" height="2.5" fill="#fff"/></svg>
        Keine Kosten, da wir alle Kosten der<br>Anträge, der Anlage und aller Arbeiten<br>übernehmen.
      </div>
      <div class="requirement">
        <span>Bereits ab einer Dachfläche von</span>
        <strong>1500 Quadratmeter!</strong>
      </div>
    </section>

    <footer class="contact">
      <h2 class="contact-heading">Worauf warten Sie noch?</h2>
      <div class="contact-rule"></div>
      <p class="contact-body">Nehmen Sie jetzt Kontakt auf für eine entsprechende Machbarkeitsprüfung. Natürlich ist auch das Kostenlos.</p>
      <div class="contact-details">
        <div>veltrano GmbH</div>
        <div>Fennstraße 47b, 48155 Münster</div>
        <div class="contact-line">
          <svg viewBox="0 0 24 24"><path d="M6.6 10.8a15 15 0 0 0 6.6 6.6l2.2-2.2a1 1 0 0 1 1-.25 11.4 11.4 0 0 0 3.6.57 1 1 0 0 1 1 1V20a1 1 0 0 1-1 1A17 17 0 0 1 3 4a1 1 0 0 1 1-1h3.5a1 1 0 0 1 1 1c0 1.25.2 2.45.57 3.57a1 1 0 0 1-.25 1z" fill="#fff"/></svg>
          <span>+49 176 528 914 03</span>
        </div>
        <div class="contact-line">
          <svg viewBox="0 0 24 24"><rect x="2" y="5" width="20" height="14" rx="2" fill="#fff"/><path d="M3 6 L12 13 L21 6" stroke="var(--green)" stroke-width="1.8" fill="none"/></svg>
          <span>info@veltrano-beispiel.de</span>
        </div>
      </div>
    </footer>
  </article>
</body>
</html>
```